Poster around the theme Vellingmark’s cat - Tessaline Computing

We need a poster so we can have it framed to be displayed on our office wall. Poster should be around the theme Vellingmark’s cat. A little bit about our company - Tessaline Computing is a Deep-Tech company developing Quantum Software for Extreme Ideas. See attached some reference images.

```html
<!DOCTYPE html>
<html lang="en">
<head>
<meta charset="utf-8">
<title>Wanted – Vellingmark’s Cat – Tessaline Computing</title>
<link rel="stylesheet" href="https://fonts.googleapis.com/css2?family=Alfa+Slab+One&family=Exo+2:wght@400;500&display=swap">
<style>
  :root {
    --wall: #e4e4e4;
    --frame: #000000;
    --paper-light: #efd9b0;
    --paper-mid: #e2bd80;
    --paper-dark: #c98f45;
    --ink: #1e1c1a;
    --rust: #8a3812;
    --brand: #ffffff;
    --art-light: #e07a1c;
    --art-dark: #a9480c;
  }
  html, body {
    margin: 0;
    padding: 0;
    width: 1200px;
    height: 1200px;
    overflow: hidden;
    background: var(--wall);
  }
  .canvas {
    position: relative;
    width: 1200px;
    height: 1200px;
  }
  .poster-frame {
    position: absolute;
    left: 177px;
    top: 51px;
    width: 848px;
    height: 1098px;
    background: var(--frame);
  }
  .paper {
    position: absolute;
    left: 219px;
    top: 84px;
    width: 774px;
    height: 1034px;
    background:
      radial-gradient(ellipse at 50% 55%, var(--paper-light) 0%, var(--paper-mid) 60%, var(--paper-dark) 100%);
    clip-path: polygon(0% 1%, 5% 0.5%, 47% 0%, 60% 0.3%, 66% 2%, 72% 0%, 100% 0%,
      100% 3%, 98.5% 8%, 100% 14%, 99% 28%, 100% 40%, 98% 56%, 100% 62%, 99% 75%, 100% 86%, 100% 100%,
      0% 100%, 0% 86%, 2% 78%, 0% 70%, 1% 60%, 0% 48%, 2.5% 44%, 0% 36%, 1% 20%, 0% 8%);
  }
  .brand {
    position: absolute;
    left: 0;
    width: 1200px;
    text-align: center;
    color: var(--brand);
    font-family: "Exo 2", sans-serif;
    font-weight: 500;
    margin: 0;
  }
  .brand-name {
    top: 118px;
    font-size: 44px;
    letter-spacing: 5px;
    line-height: 44px;
    text-transform: uppercase;
  }
  .brand-sub {
    top: 176px;
    font-size: 24px;
    letter-spacing: 1px;
    line-height: 26px;
    text-transform: uppercase;
  }
  .title-art {
    position: absolute;
    left: 0;
    top: 0;
    width: 1200px;
    height: 1200px;
  }
  .headline {
    font-family: "Alfa Slab One", serif;
    fill: var(--ink);
  }
  .headline .amp { fill: var(--rust); }
  .divider { stroke: var(--ink); stroke-width: 2; }
  .cat-illustration {
    position: absolute;
    left: 441px;
    top: 478px;
    width: 322px;
    height: 426px;
    background: radial-gradient(ellipse at 50% 45%, var(--art-light) 0%, var(--art-dark) 100%);
    box-shadow: inset 0 0 0 2px #3a1e0a;
  }
  .star { fill: var(--ink); }
</style>
</head>
<body>
<main class="canvas">
  <div class="poster-frame"></div>
  <div class="paper"></div>

  <p class="brand brand-name">Tessaline</p>
  <p class="brand brand-sub">Computing</p>

  <svg class="title-art" viewBox="0 0 1200 1200">
    <text class="headline" x="315" y="376" font-size="180" textLength="587" lengthAdjust="spacingAndGlyphs">WANTED</text>
    <text class="headline" x="412" y="430" font-size="44" textLength="381" lengthAdjust="spacingAndGlyphs">DEAD <tspan class="amp">&amp;</tspan> ALIVE</text>
    <line class="divider" x1="346" y1="458" x2="879" y2="458"/>
    <text class="headline" x="359" y="978" font-size="70" textLength="495" lengthAdjust="spacingAndGlyphs" style="font-variant: small-caps;">Vellingmark’s</text>
    <text class="headline" x="512" y="1056" font-size="74" textLength="178" lengthAdjust="spacingAndGlyphs">CAT</text>
    <g class="stars">
      <polygon class="star" points="395,1014 398,1022 406,1022 400,1027 402,1035 395,1030 388,1035 390,1027 384,1022 392,1022"/>
      <polygon class="star" points="435,1014 438,1022 446,1022 440,1027 442,1035 435,1030 428,1035 430,1027 424,1022 432,1022"/>
      <polygon class="star" points="474,1014 477,1022 485,1022 479,1027 481,1035 474,1030 467,1035 469,1027 463,1022 471,1022"/>
      <polygon class="star" points="737,1014 740,1022 748,1022 742,1027 744,1035 737,1030 730,1035 732,1027 726,1022 734,1022"/>
      <polygon class="star" points="776,1014 779,1022 787,1022 781,1027 783,1035 776,1030 769,1035 771,1027 765,1022 773,1022"/>
      <polygon class="star" points="816,1014 819,1022 827,1022 821,1027 823,1035 816,1030 809,1035 811,1027 805,1022 813,1022"/>
    </g>
  </svg>

  <div class="cat-illustration" role="img" aria-label="Illustration of a grey cat wearing round glasses, holding a quantum mechanics book, on an orange background"></div>
</main>
</body>
</html>
```